Email signature

I have an email signature, card and letter head and I would like the colours darker and more distinctive and I would like the contact details to be bigger and or easier to read as they are hard to read at the moment. The arrow watermark is fine I think.

Logo Text

VANTORA GUARD PTY LTD

Requirements
Nice to have
• The yellow type colour with the grey is good and I would like to retain that, but it looks washed out and too light on the screen. I like the arrows and I like the watermark arrows as well and I would like to retain the basic design.

```html
<!DOCTYPE html>
<html lang="en">
<head>
<meta charset="utf-8">
<title>Vantora Guard Pty Ltd – Business Card</title>
<link rel="stylesheet" href="https://fonts.googleapis.com/css2?family=Heebo:wght@300;400&display=swap">
<style>
  :root {
    --backdrop: #ececed;
    --card: #ffffff;
    --amber: #eea60e;
    --graphite: #5c5d5f;
    --graphite-soft: #7a7b7d;
    --watermark: #eef0f0;
  }
  html, body {
    margin: 0;
    width: 1200px;
    height: 1000px;
    overflow: hidden;
    background: var(--backdrop);
    font-family: "Heebo", sans-serif;
  }
  .business-card {
    position: absolute;
    left: 87px;
    top: 191px;
    width: 1028px;
    height: 618px;
    background: var(--card);
    color: var(--graphite);
    overflow: hidden;
  }
  .watermark-area {
    position: absolute;
    left: 0;
    top: 398px;
    width: 545px;
    height: 220px;
    background: linear-gradient(90deg, var(--watermark) 0%, rgba(238, 240, 240, 0.55) 70%, rgba(238, 240, 240, 0) 100%);
  }
  .business-card p { margin: 0; position: absolute; white-space: nowrap; line-height: 1; }
  .brand-name {
    left: 57px;
    top: 72px;
    font-weight: 300;
    font-size: 82px;
    letter-spacing: 1px;
    color: var(--amber);
  }
  .brand-suffix {
    right: 57px;
    top: 160px;
    font-weight: 300;
    font-size: 50px;
    letter-spacing: 4px;
    color: var(--graphite-soft);
  }
  .person-name {
    right: 57px;
    top: 294px;
    font-weight: 300;
    font-size: 48px;
  }
  .person-role {
    right: 60px;
    top: 364px;
    font-weight: 400;
    font-size: 40px;
    color: var(--amber);
  }
  .phone {
    right: 57px;
    top: 460px;
    font-weight: 400;
    font-size: 34px;
  }
  .web-contacts {
    right: 57px;
    top: 522px;
    font-weight: 400;
    font-size: 30px;
  }
  .label { color: var(--amber); }
  .gap { display: inline-block; width: 18px; }
</style>
</head>
<body>
  <section class="business-card">
    <div class="watermark-area" role="img" aria-label="Faint watermark pattern of arrows"></div>
    <p class="brand-name">VANTORA GUARD</p>
    <p class="brand-suffix">PTY LTD</p>
    <p class="person-name">LEO MARSH</p>
    <p class="person-role">DIRECTOR</p>
    <p class="phone"><span class="label">PH:</span> 0412 558 904</p>
    <p class="web-contacts"><span class="label">E:</span> leo@vantoraguard.net.au<span class="gap"></span><span class="label">W:</span> www.vantoraguard.net.au</p>
  </section>
</body>
</html>
```